Willow Crest Cosmetics - Package Design

New Beauty label needing product packaging design. Looking for elegant and stylish design to represent our premium brand.

This project is for 1 label and 1 box design. The winning designer will be assigned another project for the next product in the range. (to be paid as a new project)

This product is for "Dead Sea Mud Mask". Please see the label format and jar attached. Please note there are 2 different jars we are considering (will have a mud inside). Please feel free to choose whichever one suits your design best.

The labels and boxes are to retain the product information, such as size, ingredients etc, but is to be updated to our brand. You can move or display the other information as you wish.

the size of the dead sea mud mask color box is 72*72*85mm (length*width*height)
the size of dead sea mud mask label is 218*58mm (width*height)

Target Market(s)

Women 15 to 65

Requirements
Must have
• Must be elegant and represent our brand which is a premium beauty product.
Should not have
• Dark blue. Dark purple etc. Colours should compliment the logo

```html
<!DOCTYPE html>
<html lang="en">
<head>
<meta charset="utf-8">
<title>Willow Crest Cosmetics – Dead Sea Mud Mask Label</title>
<link href="https://fonts.googleapis.com/css2?family=Open+Sans:wght@400;600&family=Roboto+Condensed:wght@400;700&family=Oswald:wght@500&display=swap" rel="stylesheet">
<style>
  :root {
    --stage: #e4e4e4;
    --label-black: #141414;
    --band: #242424;
    --gold: #d9a637;
    --gold-light: #f2d27a;
    --gold-dark: #9c7424;
    --white: #f2f2f2;
    --silver-light: #f4f4f4;
    --silver-dark: #9a9a9a;
    --ink: #1c1c1c;
    --frame: #bdbdbd;
  }
  * { margin: 0; padding: 0; box-sizing: border-box; }
  html, body { width: 1200px; height: 885px; overflow: hidden; background: var(--stage); }
  .label {
    position: absolute; left: 30px; top: 291px; width: 1140px; height: 303px;
    background: var(--label-black); color: var(--white);
    font-family: "Open Sans", sans-serif;
  }
  .edge-band { position: absolute; left: 0; width: 100%; height: 13px; background: var(--band); }
  .edge-band.top { top: 9px; }
  .edge-band.bottom { bottom: 9px; }

  .heading { color: var(--gold); font-size: 12.5px; line-height: 15.6px; letter-spacing: .2px; }
  .caution { position: absolute; left: 56px; top: 46px; font-size: 12.5px; line-height: 15.6px; }
  .care-icons { position: absolute; left: 56px; top: 110px; display: flex; gap: 30px; align-items: center; }
  .maker { position: absolute; left: 202px; top: 202px; font-size: 11px; line-height: 13.6px; }
  .maker .heading { font-size: 11px; line-height: 13.6px; }
  .maker strong { font-weight: 600; }

  .info { position: absolute; left: 772px; width: 311px; font-size: 12.3px; line-height: 15.6px; text-align: justify; }
  .info.indications { top: 64px; }
  .info.ingredients { top: 157px; }

  .brand {
    position: absolute; left: 376px; width: 314px; top: 50px;
    display: flex; justify-content: center; align-items: center; gap: 8px;
  }
  .brand-mark { width: 12px; height: 12px; border-radius: 50%; border: 2px solid var(--gold); flex: none; }
  .brand-name {
    font-family: "Open Sans", sans-serif; font-weight: 600; font-size: 17px; line-height: 22px;
    color: var(--gold); white-space: nowrap;
  }
  .product-frame { position: absolute; left: 376px; top: 92px; }
  .product-title {
    position: absolute; left: 376px; width: 314px; top: 107px; text-align: center;
    font-family: "Oswald", sans-serif; font-weight: 500; font-size: 33px; line-height: 40px;
    letter-spacing: -.5px;
    background: linear-gradient(180deg, var(--gold-light), var(--gold) 50%, var(--gold-dark));
    -webkit-background-clip: text; background-clip: text; color: transparent;
  }
  .benefits {
    position: absolute; left: 376px; width: 314px; top: 146px; text-align: center;
    font-family: "Roboto Condensed", sans-serif; font-size: 14px; letter-spacing: -.3px;
  }
  .benefits .dot { color: var(--gold); font-size: 10px; padding: 0 3px; vertical-align: 1px; }
  .claim-pill {
    position: absolute; left: 402px; top: 182px; width: 255px; height: 25px; border-radius: 13px;
    background: linear-gradient(180deg, var(--silver-light), #cfcfcf 55%, var(--silver-dark));
    color: var(--ink); text-align: center; line-height: 25px;
    font-family: "Roboto Condensed", sans-serif; font-weight: 700; font-size: 13px;
  }
  .tagline {
    position: absolute; left: 376px; width: 314px; top: 219px; text-align: center;
    font-size: 8.6px; letter-spacing: 1.6px; font-weight: 600;
  }
  .net-weight {
    position: absolute; left: 376px; width: 314px; top: 244px; text-align: center;
    font-size: 10.5px; letter-spacing: 1.8px; font-weight: 600;
  }
</style>
</head>
<body>
  <section class="label">
    <div class="edge-band top" role="img" aria-label="Decorative woven border band"></div>
    <div class="edge-band bottom" role="img" aria-label="Decorative woven border band"></div>

    <div class="caution">
      <p class="heading">CAUTION</p>
      <p>FOR EXTERNAL USE ONLY.</p>
      <p>Keep out of reach of children.</p>
    </div>

    <div class="care-icons">
      <svg class="icon-pao" width="48" height="46" viewBox="0 0 48 46" aria-label="Use within 12 months of opening">
        <path d="M4 20 L44 20 L42 42 L6 42 Z" fill="none" stroke="#f2f2f2" stroke-width="2.5"/>
        <path d="M6 16 L36 4 L39 10 L9 22" fill="none" stroke="#f2f2f2" stroke-width="2.5"/>
        <text x="24" y="37" text-anchor="middle" fill="#f2f2f2" font-family="Open Sans, sans-serif" font-weight="600" font-size="11">12M</text>
      </svg>
      <div role="img" aria-label="Cruelty-free badge" style="width:48px;height:44px;border-radius:6px;background:#d8d8d8;"></div>
      <div role="img" aria-label="Certified organic ingredients badge" style="width:48px;height:48px;border-radius:50%;border:2px solid #d8d8d8;"></div>
    </div>

    <div class="maker">
      <p class="heading">Manufactured for</p>
      <p><strong>Company Name</strong></p>
      <p>www.website.com</p>
      <p>email@site.com</p>
    </div>

    <div class="brand">
      <span class="brand-mark" aria-hidden="true"></span>
      <p class="brand-name">Willow Crest Cosmetics</p>
    </div>

    <svg class="product-frame" width="308" height="106" viewBox="0 0 308 106" aria-hidden="true">
      <path d="M108 1 L12 1 Q1 1 1 12 L1 94 Q1 105 12 105 L296 105 Q307 105 307 94 L307 12 Q307 1 296 1 L200 1"
            fill="none" stroke="#bdbdbd" stroke-width="1.5"/>
    </svg>
    <h1 class="product-title">Dead Sea Mud Mask</h1>
    <p class="benefits">Anti Acne <span class="dot">●</span> Deep Skin Cleanser <span class="dot">●</span> Pore Reducer</p>
    <p class="claim-pill">100% natural mineral-infused detoxifier packed</p>
    <p class="tagline">WITH VITAMINS TO PROMOTE YOUTHFUL SKIN</p>
    <p class="net-weight">250G L 8.8FL.OZ</p>

    <div class="info indications">
      <p class="heading">INDICATIONS</p>
      <p>Natures Dead sea mud mask. 100% Natural &amp; Mineral-Rich Formula. Absorbs excess Oil and removes dead skin cells. Dirt and toxins revealing radiant and texture. Clarity and tone.</p>
    </div>
    <div class="info ingredients">
      <p class="heading">INGREDIENTS</p>
      <p>Deionized Water. Pure Dead Sea Mud, Kaolin. Shea Butter. Sunflower Oil, Aloe Vera Juice, Vegetable Glycerin. Jojoba Oil. Hickory Bark Extract. Calendula Oil. Xanthan Gum. Vitamin E, Hyaluronic acid.</p>
    </div>
  </section>
</body>
</html>
```